Coral Tidewave Stationary

Recently established Aquatics Club, with competitive swimming being a principal activity needs stationary, including business cards, letterhead and envelopes, application forms.
The designs shold incorporate the Club's logo. ( The colours are aqua and teal)
The statonary should be fun yet project a corporate image sufficient to attract potential sponsors.

Target Market(s)

Club members, sponsors, professional organisations.

Industry/Entity Type

Business

Requirements
Must have
• Club Logo
Address & Telephone number

The letterhead must contain the Club's Mission Statement.
It can be incorporated in the "footer" on the page.

To provide aquatics programmes, for persons of all ages, that encourage physical fitness and wellness, build character and self-discipline, inspire camaraderie and promote civic mindedness and excellence.

```html
<!DOCTYPE html>
<html lang="en">
<head>
<meta charset="UTF-8">
<title>Coral Tidewave Business Card</title>
<link rel="stylesheet" href="https://fonts.googleapis.com/css2?family=Source+Sans+3:wght@400;600;700&display=swap">
<style>
  :root {
    --backdrop: #ece7e2;
    --card-white: #ffffff;
    --orange: #f28c2e;
    --orange-deep: #ee7a1d;
    --orange-light: #f7a04a;
    --teal: #17877f;
    --ink: #4a4a4a;
    --ink-soft: #5c5c5c;
    --white: #ffffff;
  }
  * { margin: 0; padding: 0; box-sizing: border-box; }
  html, body {
    width: 1200px; height: 758px; overflow: hidden;
    background: var(--backdrop);
    font-family: "Source Sans 3", sans-serif;
  }
  .canvas { position: relative; width: 1200px; height: 758px; }

  .card {
    position: absolute;
    width: 530px; height: 305px;
    border-radius: 24px;
    overflow: hidden;
    box-shadow: 0 10px 24px rgba(0,0,0,0.18);
  }

  /* Front */
  .card-front { left: 50px; top: 226px; background: var(--card-white); }
  .front-swoosh { position: absolute; inset: 0; width: 100%; height: 100%; }

  .brand-dot {
    position: absolute; left: 40px; top: 28px;
    width: 20px; height: 20px; border-radius: 50%;
    background: var(--teal);
  }
  .brand-name {
    position: absolute; left: 40px; top: 56px;
    font-weight: 700; font-size: 42px; line-height: 1.0;
    color: var(--orange);
    width: 260px;
  }

  .holder {
    position: absolute; left: 40px; top: 180px;
    font-size: 19px; font-weight: 700; letter-spacing: 1.5px;
    color: var(--ink); white-space: nowrap;
  }
  .holder .title { font-size: 13px; font-weight: 400; letter-spacing: 0.5px; }

  .address {
    position: absolute; right: 34px; top: 26px;
    text-align: right; font-size: 13px; line-height: 1.35;
    color: var(--ink-soft);
  }

  .contacts {
    position: absolute; right: 34px; top: 180px;
    list-style: none;
    font-size: 13px; line-height: 19px; color: var(--white);
  }
  .contacts li { display: flex; justify-content: flex-end; align-items: center; gap: 6px; }
  .contacts .icon { width: 11px; height: 11px; flex: none; fill: var(--white); overflow: visible; }

  /* Back */
  .card-back {
    left: 620px; top: 226px;
    background: linear-gradient(135deg, var(--orange-light), var(--orange-deep));
  }
  .back-name {
    position: absolute; left: 0; right: 0; top: 92px;
    text-align: center; font-weight: 700; font-size: 54px; line-height: 1;
    color: var(--white);
  }
  .back-web {
    position: absolute; left: 0; right: 0; top: 210px;
    text-align: center; font-weight: 700; font-size: 20px; letter-spacing: 4px;
    color: var(--white);
  }
</style>
</head>
<body>
<main class="canvas">

  <section class="card card-front">
    <svg class="front-swoosh" viewBox="0 0 530 305" preserveAspectRatio="none" aria-hidden="true">
      <path d="M0 268 C 180 268, 360 215, 530 120 L530 305 L0 305 Z" fill="var(--orange)"/>
      <path d="M0 251 C 150 253, 270 232, 370 188 C 285 234, 160 260, 0 261 Z" fill="var(--teal)"/>
    </svg>

    <span class="brand-dot"></span>
    <div class="brand-name">Coral Tidewave</div>

    <p class="holder">YOUR NAME, <span class="title">Title</span></p>

    <p class="address">00, Complex name<br>City, State 0025</p>

    <ul class="contacts">
      <li><svg class="icon" viewBox="0 0 12 12"><circle cx="6" cy="6" r="5.5" fill="none" stroke="#fff" stroke-width="1.2"/><path d="M4 3h1.5l.5 1.6-.8.6a4 4 0 0 0 1.6 1.6l.6-.8 1.6.5V8A1 1 0 0 1 8 9 5 5 0 0 1 3 4a1 1 0 0 1 1-1z"/></svg>+09876 54321</li>
      <li><svg class="icon" viewBox="0 0 12 12"><rect x="3" y="0.5" width="6" height="11" rx="1.2"/><rect x="4" y="2" width="4" height="6" fill="var(--orange)"/></svg>+12345 67890</li>
      <li><svg class="icon" viewBox="0 0 12 12"><rect x="0.5" y="2.5" width="11" height="7.5" rx="0.8"/><path d="M1 3l5 4 5-4" fill="none" stroke="var(--orange)" stroke-width="1"/></svg>name@tidewave.com</li>
      <li><svg class="icon" viewBox="0 0 12 12"><circle cx="6" cy="6" r="5.5"/><path d="M0.5 6h11M6 0.5c-2.5 3-2.5 8 0 11M6 0.5c2.5 3 2.5 8 0 11" fill="none" stroke="var(--orange)" stroke-width="0.8"/></svg>www.website.com</li>
    </ul>
  </section>

  <section class="card card-back">
    <div class="back-name">Coral Tidewave</div>
    <p class="back-web">www.website.com</p>
  </section>

</main>
</body>
</html>
```